Product Label Design for Natural Cosmetics brand

For our company Brisamar, we are looking for a completely new label design for our natural cosmetics line made with Organic Aloe Vera.
The first product in line is Serenito, our Aloe Vera Gel. Based on the schema you create, further labels would have to be created.
Since the line includes different products (for Face, Body, Hands, Sun), there should be some color distinction between different product that can keep the products apart, having still a very similar schema.
The label should reflect the South Portuguese (Algarve) way, trust and quality. The label design should be minimalistic, well recognizable and readable, including though the following components
Logo
Product Name: Serenito (medium)
Product Function (in Portuguese mainly): GEL DE ALOÉ VERA BIO (Large and visible)
Key Infomation: For Skin and Hair
Contains 200x concentrated Aloe Vera and Organic Jojoba Oil
Following logos are to be placed on the packaging: Vegan, Organic Aloe Vera, Natural Product
Additional Info:
Barcode (EAN Number)
Ingredients (please see the current label)
Made in Portugal
Address: Check current label
QR Code for URL to open Instructions and get support
Functions and Instructions need to be in the following language:
Function: Bio Aloe Vera Gel
Instruction: External Use.
English, Spanish, French, Italian, German, Dutch, Swedish, Portuguese, Arabic
Please use google translate or put placeholders for the respective languages.
I am uploading the current label (content and design is different than what we are looking for), the package (the amber pump bottle remains the same and is available to see at https://brisamar-example.com/default/serenito-aloe-vera-gel-1.html ) and the logo.
We would like you to illustrate how the label would look on the bottle and how you plan to distinct between other products that we will be designing in the series.
Please let me know if you need anything else.

```html
<!DOCTYPE html>
<html lang="en">
<head>
<meta charset="utf-8">
<title>Serenito Aloe Vera Gel – Label Series</title>
<link rel="stylesheet" href="https://fonts.googleapis.com/css2?family=Montserrat:wght@200;300;500;600&family=Cormorant+Garamond:wght@400;500&family=Allura&display=swap">
<style>
  :root {
    --page-bg: #eceef1;
    --label-blush: #ead6cd;
    --label-lavender: #cbccdc;
    --label-sage: #c9cab5;
    --rose: #e3879b;
    --rose-muted: #c98c96;
    --ink-soft: #8f6f74;
    --mark: #9a8e86;
    --wash-blue: rgba(160, 186, 214, 0.55);
    --aloe-dark: #5f8a3a;
    --aloe-light: #a9c46a;
  }
  * { box-sizing: border-box; margin: 0; padding: 0; }
  html, body {
    width: 1200px;
    height: 921px;
    overflow: hidden;
    background: var(--page-bg);
  }
  .series {
    width: 1200px;
    height: 921px;
    display: flex;
    justify-content: center;
    align-items: center;
    gap: 40px;
  }
  .label {
    position: relative;
    width: 340px;
    height: 520px;
    overflow: hidden;
  }
  .label--face { background: var(--label-blush); }
  .label--body { background: var(--label-lavender); }
  .label--hands { background: var(--label-sage); }

  .brand {
    position: absolute;
    top: 34px;
    left: 0;
    width: 100%;
    display: flex;
    flex-direction: column;
    align-items: center;
    gap: 8px;
  }
  .brand__dot {
    width: 54px;
    height: 54px;
    border: 1.5px solid var(--mark);
    border-radius: 50%;
  }
  .brand__name {
    font-family: "Montserrat", sans-serif;
    font-weight: 500;
    font-size: 12px;
    letter-spacing: 4px;
    color: var(--mark);
  }

  .wash {
    position: absolute;
    top: 215px;
    left: 90px;
    width: 150px;
    height: 215px;
    background: var(--wash-blue);
    border-radius: 18px 40px 22px 34px;
    transform: rotate(-8deg);
  }
  .aloe {
    position: absolute;
    top: 340px;
    left: 185px;
    width: 120px;
    height: 120px;
    background: radial-gradient(ellipse at 50% 90%, var(--aloe-dark) 0%, var(--aloe-light) 55%, rgba(169,196,106,0) 72%);
  }

  .product-name {
    position: absolute;
    top: 178px;
    left: 0;
    width: 100%;
    text-align: center;
    font-family: "Cormorant Garamond", serif;
    font-weight: 500;
    font-size: 31px;
    letter-spacing: 1px;
    color: var(--rose);
  }
  .product-type {
    position: absolute;
    top: 212px;
    left: 40px;
    font-family: "Allura", cursive;
    font-size: 46px;
    line-height: 1;
    color: var(--rose);
  }
  .product-function {
    position: absolute;
    top: 246px;
    left: 40px;
    font-family: "Montserrat", sans-serif;
    font-weight: 200;
    font-size: 60px;
    line-height: 0.98;
    letter-spacing: 1px;
    color: var(--rose-muted);
  }
  .key-info {
    position: absolute;
    top: 372px;
    left: 42px;
    font-family: "Montserrat", sans-serif;
    font-weight: 300;
    font-size: 13px;
    line-height: 1.3;
    letter-spacing: 2.5px;
    color: var(--ink-soft);
  }
  .contents {
    position: absolute;
    top: 430px;
    left: 42px;
    width: 120px;
    font-family: "Montserrat", sans-serif;
    font-weight: 600;
    font-size: 7.5px;
    line-height: 1.45;
    color: var(--rose-muted);
  }
  .badges {
    position: absolute;
    top: 432px;
    left: 168px;
    display: flex;
    gap: 16px;
  }
  .badge {
    width: 20px;
    height: 20px;
    border: 1.2px solid var(--rose-muted);
    border-radius: 50%;
  }
</style>
</head>
<body>
<main class="series">

  <section class="label label--face">
    <div class="brand"><span class="brand__dot"></span><span class="brand__name">BRISAMAR</span></div>
    <div class="wash" role="img" aria-label="Soft blue watercolour wash"></div>
    <div class="product-name">SERENITO</div>
    <div class="product-type">gel</div>
    <div class="product-function">ALOÉ<br>VERA</div>
    <div class="aloe" role="img" aria-label="Illustration of an aloe vera plant"></div>
    <div class="key-info">FOR SKIN<br>AND HAIR</div>
    <p class="contents">Contains 200x concentrated Aloe Vera and Organic Jojoba Oil</p>
    <div class="badges"><span class="badge"></span><span class="badge"></span><span class="badge"></span></div>
  </section>

  <section class="label label--body">
    <div class="brand"><span class="brand__dot"></span><span class="brand__name">BRISAMAR</span></div>
    <div class="wash" role="img" aria-label="Soft blue watercolour wash"></div>
    <div class="product-name">SERENITO</div>
    <div class="product-type">gel</div>
    <div class="product-function">ALOÉ<br>VERA</div>
    <div class="aloe" role="img" aria-label="Illustration of an aloe vera plant"></div>
    <div class="key-info">FOR SKIN<br>AND HAIR</div>
    <p class="contents">Contains 200x concentrated Aloe Vera and Organic Jojoba Oil</p>
    <div class="badges"><span class="badge"></span><span class="badge"></span><span class="badge"></span></div>
  </section>

  <section class="label label--hands">
    <div class="brand"><span class="brand__dot"></span><span class="brand__name">BRISAMAR</span></div>
    <div class="wash" role="img" aria-label="Soft blue watercolour wash"></div>
    <div class="product-name">SERENITO</div>
    <div class="product-type">gel</div>
    <div class="product-function">ALOÉ<br>VERA</div>
    <div class="aloe" role="img" aria-label="Illustration of an aloe vera plant"></div>
    <div class="key-info">FOR SKIN<br>AND HAIR</div>
    <p class="contents">Contains 200x concentrated Aloe Vera and Organic Jojoba Oil</p>
    <div class="badges"><span class="badge"></span><span class="badge"></span><span class="badge"></span></div>
  </section>

</main>
</body>
</html>
```